I need the following
2 versions (CMYK and RGB)
Full Page ad design 7.5" wide x 10" tall
No less than 300 dpi for print and 72dpi for web:
Full Color CMYK for print and RGB for web
Provide a high quality JPEG of the ad as well.

You can use the attached post card as a guide and use the info within it. You can get more information from our website at HaulingCrewFolks.net.
Also add a block with the following ... We work with real estate agents to make moving stress - free for their clients:
*Old Fashioned Customer Service
*Discounted rates
*Always Free Estimates
*Fully Licensed and Insured
*Communication From Start To Finish
*Full Service Moving

```html
<!DOCTYPE html>
<html lang="en">
<head>
<meta charset="utf-8">
<title>Hauling Crew Folks – Full Page Ad</title>
<link href="https://fonts.googleapis.com/css2?family=Poppins:wght@400;500;600;700;800&display=swap" rel="stylesheet">
<style>
  :root{
    --orange:#f0a24a;
    --orange-deep:#e8922e;
    --charcoal:#333131;
    --charcoal-dark:#262424;
    --ink:#3a3232;
    --grey-panel:#e6e6e6;
    --white:#ffffff;
    --page-bg:#f1f0ed;
  }
  *{margin:0;padding:0;box-sizing:border-box}
  html,body{width:1200px;height:2400px;overflow:hidden}
  body{background:var(--page-bg);font-family:'Poppins',sans-serif;color:var(--ink);position:relative}

  .ad{position:absolute;left:0;top:400px;width:1200px;height:1600px;background:var(--white);overflow:hidden;box-shadow:0 6px 24px rgba(0,0,0,.12)}

  .hero{position:absolute;left:0;top:0;width:1200px;height:573px;background:linear-gradient(180deg,#3a3836 0%,#2f2d2c 60%,#343231 100%)}
  .hero-photo{position:absolute;inset:0;background:radial-gradient(ellipse at 55% 60%,rgba(90,88,86,.35),rgba(0,0,0,0) 60%)}

  .brand{position:absolute;left:75px;top:80px;display:flex;align-items:center;gap:14px;font-weight:600;font-size:42px;color:var(--orange);letter-spacing:.5px}
  .brand-mark{width:26px;height:26px;border-radius:50%;background:var(--orange)}

  .headline{position:absolute;left:75px;top:200px;line-height:1}
  .headline .lead{display:block;font-weight:400;font-size:76px;color:var(--white);letter-spacing:1px}
  .headline .strong{display:block;font-weight:800;font-size:90px;color:var(--white);margin-top:10px}
  .headline .accent{display:block;font-weight:800;font-size:90px;color:var(--orange);margin-top:4px}

  .license{position:absolute;left:75px;top:491px;height:48px;display:flex;border-radius:24px;overflow:hidden;font-weight:500;font-size:31px}
  .license .label{background:var(--orange);color:var(--charcoal);padding:0 10px 0 18px;display:flex;align-items:center}
  .license .number{background:var(--white);color:var(--charcoal);padding:0 22px 0 14px;display:flex;align-items:center;border-radius:0 24px 24px 0}

  .hand-truck{position:absolute;left:700px;top:100px;width:490px;height:560px;background:linear-gradient(160deg,#d7bf9c 0%,#c2a57d 55%,#8a7a63 100%);clip-path:polygon(52% 0,100% 8%,100% 40%,88% 90%,70% 100%,20% 82%,0 62%,28% 40%);z-index:2}

  .testimonial{position:absolute;left:73px;top:614px;width:1062px;height:205px;background:var(--grey-panel);padding:38px 38px 0 38px;font-size:20.5px;line-height:1.17;color:var(--charcoal)}
  .testimonial .author{display:block;color:var(--orange-deep);font-weight:600;margin-top:2px}
  .quote-mark{position:absolute;font-weight:800;font-size:70px;color:#8a8a8a;line-height:1}
  .quote-open{left:68px;top:580px}
  .quote-close{left:1093px;top:808px}

  .coupon{position:absolute;top:853px;width:333px;height:176px}
  .coupon svg{position:absolute;inset:0}
  .coupon .txt{position:absolute;inset:0;text-align:center;padding-top:14px;line-height:1}
  .coupon .off{display:block;font-weight:700;font-size:54px;color:var(--white)}
  .coupon .off sup{font-size:25px;vertical-align:top;position:relative;top:4px}
  .coupon .under{display:block;font-weight:700;font-size:28px;color:var(--orange);margin-top:4px}
  .coupon .price{display:block;font-weight:700;font-size:30px;color:var(--white);margin-top:4px}
  .coupon .fine{display:block;font-size:12.5px;color:var(--white);margin-top:8px}
  .coupon.is-featured .under{color:var(--charcoal)}
  .coupon-25{left:99px}
  .coupon-50{left:432px}
  .coupon-100{left:765px}

  .agents-note{position:absolute;left:0;top:1040px;width:1200px;text-align:center;font-weight:600;font-size:19px;color:var(--charcoal)}
  .agents-note em{font-style:normal;color:var(--orange-deep)}

  .features{position:absolute;left:0;top:1114px;width:1200px;height:228px;background:var(--orange)}
  .feature{position:absolute;top:0;width:170px;transform:translateX(-50%);text-align:center}
  .feature .hex{position:absolute;left:50%;top:-36px;transform:translateX(-50%);width:80px;height:80px}
  .feature .name{position:absolute;left:0;right:0;top:66px;font-weight:700;font-size:21.5px;line-height:1.26;color:var(--ink);text-transform:uppercase}
  .divider{position:absolute;top:36px;height:180px;border-left:2px dotted rgba(255,255,255,.75)}

  .benefits{position:absolute;top:1368px;list-style:none;font-size:22px;line-height:1.22;color:var(--charcoal)}
  .benefits li{position:relative;padding-left:32px;margin-bottom:12px}
  .benefits li::before{content:"";position:absolute;left:0;top:7px;width:13px;height:13px;border-radius:50%;background:var(--orange);box-shadow:inset 0 0 0 3px #fbd8ad}
  .benefits-left{left:83px;width:500px}
  .benefits-right{left:604px;width:560px}

  .phone{position:absolute;left:0;top:1472px;width:522px;height:70px;background:var(--orange);border-radius:0 35px 35px 0;display:flex;align-items:center;padding-left:72px;gap:14px;font-weight:600;font-size:40px;color:var(--charcoal)}
  .phone svg{width:42px;height:42px}

  .contact{position:absolute;left:668px;top:1471px;list-style:none;font-weight:600;font-size:22px;color:var(--charcoal)}
  .contact li{display:flex;align-items:center;gap:14px;height:40px}
  .contact svg{width:28px;height:28px}
</style>
</head>
<body>
<main class="ad">

  <section class="hero">
    <div class="hero-photo" role="img" aria-label="Darkened photo of a moving truck parked outside a building"></div>

    <div class="brand"><span class="brand-mark"></span><span>Hauling Crew Folks</span></div>

    <h1 class="headline">
      <span class="lead">WE ARE</span>
      <span class="strong">READY FOR</span>
      <span class="accent">YOUR MOVE</span>
    </h1>

    <div class="license"><span class="label">TXDMV:</span><span class="number">004218835B</span></div>
  </section>

  <div class="hand-truck" role="img" aria-label="Photo of stacked cardboard boxes on a blue hand truck"></div>

  <span class="quote-mark quote-open">&ldquo;</span>
  <blockquote class="testimonial">
    Best movers in Dallas! They were fast, efficient, on time and very<br>
    reasonably priced. They took so much care with our belongings.<br>
    We have moved about 15 times and they are the best movers we have ever had.<br>
    Highly recommend to anyone looking for movers. We really appreciate the care that they<br>
    handled our furniture with. We will definitely be using them again. Thank you Sam and team!
    <span class="author">-DANA WHITFIELD</span>
  </blockquote>
  <span class="quote-mark quote-close">&rdquo;</span>

  <div class="coupon coupon-25">
    <svg viewBox="0 0 333 176" aria-hidden="true">
      <path d="M24,0 H309 A24,24 0 0 0 333,24 V152 A24,24 0 0 0 309,176 H24 A24,24 0 0 0 0,152 V24 A24,24 0 0 0 24,0 Z" fill="#333131"/>
      <path d="M34,10 H299 A24,24 0 0 0 323,34 V142 A24,24 0 0 0 299,166 H34 A24,24 0 0 0 10,142 V34 A24,24 0 0 0 34,10 Z" fill="none" stroke="#fff" stroke-width="2"/>
    </svg>
    <div class="txt"><span class="off"><sup>$</sup>25 OFF</span><span class="under">MOVES UNDER</span><span class="price">$500</span><span class="fine">With this card. Call for details.</span></div>
  </div>

  <div class="coupon coupon-50 is-featured">
    <svg viewBox="0 0 333 176" aria-hidden="true">
      <path d="M24,0 H309 A24,24 0 0 0 333,24 V152 A24,24 0 0 0 309,176 H24 A24,24 0 0 0 0,152 V24 A24,24 0 0 0 24,0 Z" fill="#f0a24a"/>
      <path d="M34,10 H299 A24,24 0 0 0 323,34 V142 A24,24 0 0 0 299,166 H34 A24,24 0 0 0 10,142 V34 A24,24 0 0 0 34,10 Z" fill="none" stroke="#fff" stroke-width="2"/>
    </svg>
    <div class="txt"><span class="off"><sup>$</sup>50 OFF</span><span class="under">MOVES UNDER</span><span class="price">$500</span><span class="fine">With this card. Call for details.</span></div>
  </div>

  <div class="coupon coupon-100">
    <svg viewBox="0 0 333 176" aria-hidden="true">
      <path d="M24,0 H309 A24,24 0 0 0 333,24 V152 A24,24 0 0 0 309,176 H24 A24,24 0 0 0 0,152 V24 A24,24 0 0 0 24,0 Z" fill="#333131"/>
      <path d="M34,10 H299 A24,24 0 0 0 323,34 V142 A24,24 0 0 0 299,166 H34 A24,24 0 0 0 10,142 V34 A24,24 0 0 0 34,10 Z" fill="none" stroke="#fff" stroke-width="2"/>
    </svg>
    <div class="txt"><span class="off"><sup>$</sup>100 OFF</span><span class="under">MOVES UNDER</span><span class="price">$500</span><span class="fine">With this card. Call for details.</span></div>
  </div>

  <p class="agents-note">We work with <em>real estate agents</em> to make moving stress-free for their clients:</p>

  <section class="features">
    <span class="divider" style="left:221px"></span>
    <span class="divider" style="left:394px"></span>
    <span class="divider" style="left:580px"></span>
    <span class="divider" style="left:813px"></span>
    <span class="divider" style="left:989px"></span>

    <div class="feature" style="left:137px">
      <svg class="hex" viewBox="0 0 80 80" aria-hidden="true"><polygon points="40,3 74,21 74,59 40,77 6,59 6,21" fill="#333131" stroke="#fff" stroke-width="4"/><rect x="27" y="26" width="26" height="28" rx="3" fill="#fff"/><path d="M32,34h16M32,40h16M32,46h10" stroke="#333131" stroke-width="2.5"/></svg>
      <p class="name">Old<br>Fashioned<br>Customer<br>Service</p>
    </div>
    <div class="feature" style="left:308px">
      <svg class="hex" viewBox="0 0 80 80" aria-hidden="true"><polygon points="40,3 74,21 74,59 40,77 6,59 6,21" fill="#333131" stroke="#fff" stroke-width="4"/><path d="M40,22 l10,4 v8 c0,6 -4,10 -10,12 c-6,-2 -10,-6 -10,-12 v-8z" fill="#fff"/><path d="M35,34 l4,4 l7,-7" stroke="#333131" stroke-width="2.5" fill="none"/><circle cx="28" cy="50" r="5" fill="#fff"/><circle cx="52" cy="50" r="5" fill="#fff"/><path d="M20,60 a8,6 0 0 1 16,0z M44,60 a8,6 0 0 1 16,0z" fill="#fff"/></svg>
      <p class="name">Fully<br>Licensed<br>and<br>Insured</p>
    </div>
    <div class="feature" style="left:487px">
      <svg class="hex" viewBox="0 0 80 80" aria-hidden="true"><polygon points="40,3 74,21 74,59 40,77 6,59 6,21" fill="#333131" stroke="#fff" stroke-width="4"/><path d="M26,42 l16,-16 h12 v12 l-16,16z" fill="#fff"/><circle cx="49" cy="31" r="2.5" fill="#333131"/><path d="M35,44 l8,-8" stroke="#333131" stroke-width="2.5"/></svg>
      <p class="name">Discounted<br>Rates</p>
    </div>
    <div class="feature" style="left:692px">
      <svg class="hex" viewBox="0 0 80 80" aria-hidden="true"><polygon points="40,3 74,21 74,59 40,77 6,59 6,21" fill="#333131" stroke="#fff" stroke-width="4"/><path d="M24,28 h24 v16 h-16 l-6,6 v-6 h-2z" fill="#fff"/><path d="M50,34 h6 v14 h-2 v5 l-5,-5 h-13 v-2" fill="#fff"/><path d="M29,36h14" stroke="#333131" stroke-width="2.5"/></svg>
      <p class="name">Communication<br>From Start<br>To Finish</p>
    </div>
    <div class="feature" style="left:904px">
      <svg class="hex" viewBox="0 0 80 80" aria-hidden="true"><polygon points="40,3 74,21 74,59 40,77 6,59 6,21" fill="#333131" stroke="#fff" stroke-width="4"/><path d="M24,44 l18,-18 h12 v12 l-18,18z" fill="#fff"/><circle cx="49" cy="31" r="2.5" fill="#333131"/></svg>
      <p class="name">Always<br>Free<br>Estimates</p>
    </div>
    <div class="feature" style="left:1076px">
      <svg class="hex" viewBox="0 0 80 80" aria-hidden="true"><polygon points="40,3 74,21 74,59 40,77 6,59 6,21" fill="#333131" stroke="#fff" stroke-width="4"/><rect x="22" y="28" width="24" height="20" fill="#fff"/><path d="M46,34 h8 l5,7 v7 h-13z" fill="#fff"/><circle cx="30" cy="51" r="4" fill="#fff" stroke="#333131" stroke-width="2"/><circle cx="52" cy="51" r="4" fill="#fff" stroke="#333131" stroke-width="2"/></svg>
      <p class="name">Full<br>Service<br>Moving</p>
    </div>
  </section>

  <ul class="benefits benefits-left">
    <li>Save time and effort with packing services</li>
    <li>Keep your belongings safe with<br>reputable movers</li>
  </ul>
  <ul class="benefits benefits-right">
    <li>Save money with our cost-effective pricing</li>
    <li>Fully licensed and insured</li>
  </ul>

  <div class="phone">
    <svg viewBox="0 0 42 42" aria-hidden="true"><circle cx="21" cy="21" r="20" fill="#333131"/><path d="M14,12 l5,0 l2,6 l-3,2 c1,3 3,5 6,6 l2,-3 l6,2 l0,5 c-10,1 -19,-8 -18,-18z" fill="#fff"/></svg>
    <span>(972) 555-0147</span>
  </div>

  <ul class="contact">
    <li><svg viewBox="0 0 28 28" aria-hidden="true"><rect x="3" y="7" width="22" height="16" rx="2" fill="#333131"/><path d="M4,9 l10,7 l10,-7" stroke="#fff" stroke-width="2" fill="none"/></svg>haulingcrewfolks1@mailbox.net</li>
    <li><svg viewBox="0 0 28 28" aria-hidden="true"><circle cx="14" cy="14" r="11" fill="none" stroke="#333131" stroke-width="2.5"/><ellipse cx="14" cy="14" rx="5" ry="11" fill="none" stroke="#333131" stroke-width="2"/><path d="M3,14h22M5,8h18M5,20h18" stroke="#333131" stroke-width="2"/></svg>haulingcrewfolks.net</li>
  </ul>

</main>
</body>
</html>
```